Korvane Sky Works, LLC - Business Card

I currently have a drone business that specializes in aerial photography, thermal image inspections, deer recovery, search and rescue, custom agricultural applications. i will attach my current business card as well as some logos to incorporate for a new up to date business card
Updates

Designs look the same

Sick

Target Market(s)

farmers, hunters

Contact Information for Business Card

name address phone number (as existing card i attached)

Requirements
Must have
• im good with existing business card, but would like an agricultural twist

```html
<!DOCTYPE html>
<html lang="en">
<head>
<meta charset="utf-8">
<title>Korvane Sky Works, LLC – Business Card</title>
<link href="https://fonts.googleapis.com/css2?family=Montserrat:wght@400;500;700;800&display=swap" rel="stylesheet">
<style>
  :root {
    --stage: #2b2b2b;
    --card-dark: #111111;
    --card-light: #ffffff;
    --green: #3a9a35;
    --ink: #2a2a2a;
    --pattern: #1c1c1c;
  }
  * { box-sizing: border-box; margin: 0; padding: 0; }
  html, body { width: 1200px; height: 875px; overflow: hidden; }
  body {
    background: var(--stage);
    font-family: "Montserrat", sans-serif;
    position: relative;
  }
  .card {
    position: absolute;
    top: 289px;
    width: 520px;
    height: 297px;
    border-radius: 18px;
    overflow: hidden;
  }
  .card-back { left: 50px; background: var(--card-dark); }
  .card-front { left: 630px; background: var(--card-light); color: var(--ink); }

  .back-pattern {
    position: absolute; inset: 0;
    background: radial-gradient(ellipse at 30% 40%, #262626 0%, var(--pattern) 60%, var(--card-dark) 100%);
  }
  .back-mark {
    position: absolute; top: 50%; left: 50%;
    transform: translate(-50%, -50%);
    display: flex; align-items: center; gap: 8px;
  }
  .mark-dot { width: 14px; height: 14px; border-radius: 50%; background: var(--green); }
  .mark-name { color: var(--green); font-weight: 800; font-size: 24px; letter-spacing: 1px; text-transform: uppercase; }

  .front-brand {
    position: absolute; left: 30px; top: 78px; width: 180px;
    display: flex; align-items: center; gap: 8px;
  }
  .front-brand .mark-dot { width: 18px; height: 18px; }
  .front-brand .mark-name { font-size: 28px; }

  .divider {
    position: absolute; left: 222px; top: 30px; width: 1px; height: 160px;
    background: var(--green);
  }
  .contact { position: absolute; left: 240px; top: 30px; }
  .person-name { color: var(--green); font-weight: 800; font-size: 22px; letter-spacing: 0.5px; text-transform: uppercase; line-height: 1.1; }
  .person-role { font-size: 12px; margin-bottom: 10px; }
  .contact-list { list-style: none; font-size: 11.5px; line-height: 1.35; }
  .contact-list li { display: flex; align-items: flex-start; gap: 8px; margin-bottom: 5px; }
  .icon { width: 14px; height: 14px; flex: none; margin-top: 1px; }

  .services {
    position: absolute; left: 30px; right: 20px; bottom: 30px;
    font-size: 12.5px; line-height: 1.7; text-align: center;
  }
  .services span { white-space: nowrap; margin: 0 5px; }
  .services span::before { content: "\25CF"; color: var(--green); margin-right: 3px; font-size: 9px; vertical-align: 2px; }
</style>
</head>
<body>
  <section class="card card-back" aria-label="Card back">
    <div class="back-pattern" role="img" aria-label="Faint repeated brand mark pattern across the dark card"></div>
    <div class="back-mark">
      <span class="mark-dot"></span>
      <span class="mark-name">Korvane</span>
    </div>
  </section>

  <section class="card card-front" aria-label="Card front">
    <div class="front-brand">
      <span class="mark-dot"></span>
      <span class="mark-name">Korvane</span>
    </div>
    <div class="divider"></div>
    <div class="contact">
      <p class="person-name">Dalen Morrow</p>
      <p class="person-role">Owner</p>
      <ul class="contact-list">
        <li>
          <svg class="icon" viewBox="0 0 16 16"><circle cx="8" cy="8" r="7" fill="none" stroke="var(--green)" stroke-width="1.3"/><path d="M8 4a2.5 2.5 0 0 0-2.5 2.5C5.5 8.5 8 11.5 8 11.5s2.5-3 2.5-5A2.5 2.5 0 0 0 8 4z" fill="var(--green)"/></svg>
          <span>214 W. Market St.<br>Arden, OH 45900</span>
        </li>
        <li>
          <svg class="icon" viewBox="0 0 16 16"><circle cx="8" cy="8" r="7" fill="none" stroke="var(--green)" stroke-width="1.3"/><path d="M5.5 4.5l1.5 0 .7 1.8-1 .8a5 5 0 0 0 2.2 2.2l.8-1 1.8.7v1.5c0 .5-.5 1-1 1A6 6 0 0 1 4.5 5.5c0-.5.5-1 1-1z" fill="var(--green)"/></svg>
          <span>419-555-0148</span>
        </li>
        <li>
          <svg class="icon" viewBox="0 0 16 16"><circle cx="8" cy="8" r="7" fill="none" stroke="var(--green)" stroke-width="1.3"/><rect x="4.5" y="5.5" width="7" height="5" fill="none" stroke="var(--green)" stroke-width="1"/><path d="M4.5 5.5L8 8.5l3.5-3" fill="none" stroke="var(--green)" stroke-width="1"/></svg>
          <span>korvaneskyworks@mailbox.com</span>
        </li>
        <li>
          <svg class="icon" viewBox="0 0 16 16"><circle cx="8" cy="8" r="7" fill="none" stroke="var(--green)" stroke-width="1.3"/><circle cx="8" cy="8" r="3.5" fill="none" stroke="var(--green)" stroke-width="1"/><path d="M4.5 8h7M8 4.5v7" stroke="var(--green)" stroke-width="0.8"/></svg>
          <span>www.korvaneskyworks.com</span>
        </li>
      </ul>
    </div>
    <p class="services">
      <span>Thermal Image Inspections</span><span>Deer Recovery</span><span>Search &amp; Rescue</span><br>
      <span>Real Estate Photography</span>
    </p>
  </section>
</body>
</html>
```